Supplement Label Design - Sports Nutrition

Design a sports nutrition/weight loss supplement label that stands out in a crowded space. Supplement bottle size is 200c and label size is 7" x 2.5" approximately. We're looking for a design that emphasizes the products name called VYK. Vyk is an abbreviation for Vigor, Yield & Kinetics. We want VYK to be the center/focus point of the bottle and have a memorable design to it.

Target Market(s)

Men & Women over 18

Industry/Entity Type

Supplement

Font styles to use
Sans Serif
Decorative

Requirements
Must have
• Emphasis on the product name VYK. Serious, Inspirational & Motivational feel to the design, typo & colors. Electrocution/lightning feel to the text. Right hand side of label is our formulation. Left hand side is dedicated to explaining the trifecta formulation idea.
Nice to have
• For example, we like the graphic design of "Drum" energy drinks because you can identify the bottle from a distance and is memorable. We think that less is more and we'd like the design/colors do most of the talking.
Should not have
• Cartroon/animated style.

```html
<!DOCTYPE html>
<html lang="en">
<head>
<meta charset="utf-8">
<title>VYK – Supplement Label</title>
<link rel="stylesheet" href="https://fonts.googleapis.com/css2?family=Abel&family=Archivo+Black&family=Archivo+Narrow:ital,wght@0,400;0,700;1,400&family=Questrial&display=swap">
<style>
  :root {
    --page: #e6e7e8;
    --label-black: #0c0c0c;
    --red: #b51f28;
    --white: #ffffff;
    --ink: #111111;
    --rule: #9a9a9a;
  }
  * { margin: 0; padding: 0; box-sizing: border-box; }
  html, body { width: 1112px; height: 1200px; overflow: hidden; }
  body { background: var(--page); position: relative; }

  .label {
    position: absolute; left: 26px; top: 411px;
    width: 1060px; height: 378px;
    background: var(--label-black);
    overflow: hidden;
  }
  .label-art { position: absolute; inset: 0; width: 100%; height: 100%; }
  .headline-arc { font-family: "Questrial", sans-serif; font-size: 25px; fill: var(--white); letter-spacing: 0.5px; }
  .product-name { font-family: "Questrial", sans-serif; font-size: 190px; fill: var(--white); }
  .tagline-small { font-family: "Questrial", sans-serif; font-size: 21px; fill: var(--white); letter-spacing: 1px; }
  .tagline-large { font-family: "Questrial", sans-serif; font-size: 31px; fill: var(--white); letter-spacing: 0.5px; }

  /* Left: formulation story */
  .story { position: absolute; left: 32px; top: 42px; width: 294px; color: var(--white); font-family: "Abel", sans-serif; }
  .story-title { font-size: 19px; font-weight: 400; margin-bottom: 8px; letter-spacing: 0.3px; }
  .story-body { font-size: 11.4px; line-height: 14.7px; text-align: justify; letter-spacing: 0.2px; }
  .story-callout {
    position: absolute; left: 31px; top: 204px; width: 296px; height: 64px;
    border: 1.5px solid var(--white);
    padding: 8px 14px 0 17px;
    color: var(--white); font-family: "Abel", sans-serif; font-size: 10.8px; line-height: 15px; letter-spacing: 0.2px;
  }
  .story-panel { position: absolute; left: 32px; top: 279px; width: 134px; height: 68px; background: var(--white); }
  .story-note {
    position: absolute; left: 181px; top: 290px; width: 140px;
    color: var(--white); font-family: "Abel", sans-serif; font-size: 10.8px; line-height: 15px; letter-spacing: 0.2px;
  }

  /* Right: supplement facts */
  .facts {
    position: absolute; left: 763px; top: 23px; width: 264px; height: 253px;
    background: var(--white); color: var(--ink);
    border: 1px solid var(--rule);
    padding: 3px 5px 0 4px;
    font-family: "Archivo Narrow", sans-serif; font-size: 7.2px; line-height: 11px;
  }
  .facts-title { font-family: "Archivo Black", sans-serif; font-size: 22px; line-height: 25px; letter-spacing: 0.3px; margin-bottom: 2px; }
  .facts-row { display: flex; border-top: 0.5px solid #cfcfcf; }
  .facts-row.no-rule { border-top: none; }
  .facts-row .name { flex: 1; white-space: nowrap; overflow: hidden; }
  .facts-row .amt { width: 20px; text-align: right; }
  .facts-row .unit { width: 20px; text-align: center; }
  .facts-row .dv { width: 24px; text-align: right; }
  .facts-row.blend .name, .facts-row.blend .amt, .facts-row.blend .unit { font-weight: 700; }
  .facts-row.sub .name { padding-left: 6px; }
  .facts-row.split { justify-content: space-between; }
  .facts-row.thick { border-top: 1.5px solid var(--ink); }
  .facts-foot { border-top: 1.5px solid var(--ink); }

  .other-ingredients {
    position: absolute; left: 763px; top: 280px; width: 270px;
    color: var(--white); font-family: "Archivo Narrow", sans-serif; font-size: 7.4px;
  }
  .seal-row { position: absolute; left: 760px; top: 311px; display: flex; gap: 19px; }
  .seal { width: 50px; height: 50px; border-radius: 50%; background: var(--white); }
</style>
</head>
<body>
  <main class="label">
    <svg class="label-art" viewBox="0 0 1060 378">
      <defs>
        <path id="headline-curve" d="M330 36 Q537 60 745 32"/>
      </defs>

      <path class="band-top" d="M210 0 L870 0 C760 56 640 76 540 76 C440 76 320 56 210 0 Z" fill="var(--red)"/>
      <path class="band-bottom" d="M170 378 C300 316 430 294 530 294 C630 294 770 316 890 378 Z" fill="var(--red)"/>

      <text class="headline-arc" text-anchor="middle"><textPath href="#headline-curve" startOffset="50%">YIELD &amp; KINETICS</textPath></text>
      <text class="product-name" x="537" y="258" text-anchor="middle" textLength="310" lengthAdjust="spacingAndGlyphs">VYK</text>
      <text class="tagline-small" x="530" y="318" text-anchor="middle">WEIGHT LOSS</text>
      <text class="tagline-large" x="530" y="349" text-anchor="middle">SUPPLEMENT</text>
    </svg>

    <section class="story">
      <h2 class="story-title">Lorem ipsum</h2>
      <p class="story-body">Lorem ipsum dolor sit amet, consectetuer adipiscing elit, sed diam nonummy nibh euismod tincidunt ut laoreet dolore magna aliquam erat volutpat. Ut wisi enim ad minim veniam, quis nostrud exerci tation. Lorem ipsum dolor sit amet, consectetuer adipiscing elit, sed diam nonummy nibh euismod tincidunt ut laoreet dolore magna aliquam erat volutpat. Ut wisi enim ad minim veniam, quis nostrud exerci tation</p>
    </section>
    <p class="story-callout">Lorem ipsum dolor sit amet, consectetuer adipiscing elit, sed diam nonummy nibh euismod tincidunt ut laoreet dolore magna aliquam erat volutpat.</p>
    <div class="story-panel"></div>
    <p class="story-note">Lorem ipsum dolor amet, consecter adipiscing elit, aliquam erat.</p>

    <section class="facts">
      <h3 class="facts-title">Supplement Facts</h3>
      <div class="facts-row split thick"><span>Serving Size: 2 capsules</span><span>Servings Per Container: 30</span></div>
      <div class="facts-row"><span class="name">Amount per Serving</span><span class="dv">%DV</span></div>
      <div class="facts-row thick"><span class="name">Niacin (as niacinamide)</span><span class="amt">40</span><span class="unit">mg</span><span class="dv">250%</span></div>
      <div class="facts-row no-rule"><span class="name">Vitamin B6 (as pyridoxal-5-phosphate)</span><span class="amt">8.5</span><span class="unit">mg</span><span class="dv">500%</span></div>
      <div class="facts-row no-rule"><span class="name">Vitamin B12 (as methylcobalamin)</span><span class="amt">12</span><span class="unit">mcg</span><span class="dv">500%</span></div>
      <div class="facts-row blend thick"><span class="name">Proprietary Vigor Blend</span><span class="amt">450</span><span class="unit">mg</span><span class="dv">*</span></div>
      <div class="facts-row sub no-rule"><span class="name">Ashwagandha Root Extract (<i>Withania somnifera</i>)</span><span class="dv">*</span></div>
      <div class="facts-row sub no-rule"><span class="name">Acetyl L-Carnitine HCl</span><span class="dv">*</span></div>
      <div class="facts-row sub no-rule"><span class="name">L-Theanine</span><span class="dv">*</span></div>
      <div class="facts-row blend thick"><span class="name">Proprietary Yield Blend</span><span class="amt">425</span><span class="unit">mg</span><span class="dv">*</span></div>
      <div class="facts-row sub no-rule"><span class="name"><i>Garcinia cambogia</i> extract (fruit)</span><span class="dv">*</span></div>
      <div class="facts-row sub no-rule"><span class="name">Yohimbe Bark Extract (<i>Pausinystalia johimbe</i>)</span><span class="dv">*</span></div>
      <div class="facts-row sub no-rule"><span class="name">Capsivor® (capsicum fruit extract)</span><span class="dv"></span></div>
      <div class="facts-row sub no-rule"><span class="name">(standardized to 2% capsaicinoids)</span><span class="amt">320</span><span class="unit">mg</span><span class="dv"></span></div>
      <div class="facts-row blend thick"><span class="name">Proprietary Kinetics Blend (215 mg Caffeine)</span><span class="dv">*</span></div>
      <div class="facts-row sub no-rule"><span class="name">Green Tea Extract</span><span class="dv">*</span></div>
      <div class="facts-row sub no-rule"><span class="name">Theobromine</span><span class="dv">*</span></div>
      <div class="facts-row sub no-rule"><span class="name">Green Coffee Fruit Extract</span><span class="dv">*</span></div>
      <div class="facts-row facts-foot"><span class="name">*Daily Value (DV) not established</span></div>
    </section>
    <p class="other-ingredients">Other Ingredients: Rice flour, L-leucine, hypromellose (capsule).</p>
    <div class="seal-row">
      <span class="seal"></span><span class="seal"></span><span class="seal"></span><span class="seal"></span>
    </div>
  </main>
</body>
</html>
```